Zielgruppe
Verkauf und Einbau von Fenstern, Haustüren, Rollläden, Raffstore, Markisen, Insektenschutzgitter, Plissees
Aufgabenstellung
Es soll das gleiche Farbschema meines Firmenlogos haben. Grauer Hintergrund, kleine gelbe Akzente und schwarze Schrift

```html
<!DOCTYPE html>
<html lang="de">
<head>
<meta charset="utf-8">
<title>Wandelraum – Fenster, Haustüren, Sonnenschutz</title>
<link href="https://fonts.googleapis.com/css2?family=Raleway:wght@400;500;600;700;800&display=swap" rel="stylesheet">
<style>
:root{
  --yellow:#fcc30b;
  --black:#000;
  --ink:#111;
  --tile:#ececec;
  --white:#fff;
}
*{box-sizing:border-box;margin:0;padding:0}
html,body{width:1200px;height:3641px;overflow:hidden}
body{font-family:"Raleway",sans-serif;color:var(--ink);background:var(--white);position:relative}
.abs{position:absolute}
.center{text-align:center}

/* hero */
.hero{left:0;top:0;width:1200px;height:686px;
  background:
    radial-gradient(ellipse 420px 300px at 1080px 560px,rgba(176,138,88,.85),rgba(176,138,88,0) 70%),
    radial-gradient(ellipse 500px 260px at 420px 200px,rgba(120,128,110,.55),rgba(120,128,110,0) 70%),
    radial-gradient(ellipse 380px 220px at 300px 520px,rgba(235,235,232,.7),rgba(235,235,232,0) 70%),
    linear-gradient(100deg,#6f6f6c 0%,#a9a8a4 22%,#d9d7d2 48%,#cfccc6 70%,#b7ad9c 100%)}
.hero-shade{left:0;top:0;width:1200px;height:686px;background:linear-gradient(rgba(0,0,0,.18),rgba(0,0,0,.05) 40%,rgba(0,0,0,.12))}
.hero-bar{left:0;top:0;width:1200px;height:50px;background:rgba(35,35,35,.88);border-top:5px solid var(--yellow)}
.nav a{position:absolute;top:17px;color:var(--white);font-size:15px;font-weight:500;text-decoration:none}
.brand{left:66px;top:0;width:176px;height:138px;background:var(--white);border-radius:0 0 14px 14px;display:flex;flex-direction:column;align-items:center;justify-content:center;gap:10px}
.brand-mark{width:30px;height:30px;border:3px solid var(--yellow)}
.brand-name{color:var(--yellow);font-size:17px;font-weight:600;letter-spacing:.5px}
.hero-title{left:0;width:1200px;top:262px;font-size:48px;font-weight:500;color:var(--yellow)}
.hero-sub{left:0;width:1200px;top:322px;font-size:48px;font-weight:500;color:var(--white)}
.hero-sub b{font-weight:800}
.hero-text{left:0;width:1200px;top:400px;font-size:17px;font-weight:500;color:var(--white);line-height:22px}
.dots span{display:inline-block;width:9px;height:9px;border-radius:50%;margin:0 4px}

/* partners */
.partners{left:0;top:686px;width:1200px;height:633px;background:var(--black)}
.partners h2{position:absolute;left:66px;top:40px;color:var(--yellow);font-size:31px;font-weight:500;line-height:38px}
.arrow{position:absolute}
.pcard{position:absolute;width:334px;text-align:center;color:var(--white)}
.pcard .photo{height:220px;border-radius:20px}
.pcard h3{font-size:23px;font-weight:500;margin-top:16px}
.pcard p{font-size:15px;line-height:19px;margin-top:6px;font-weight:500}

/* products */
.products{left:0;top:1319px;width:1200px;height:1405px;background:linear-gradient(#fff 0%,#f1f1f1 100%)}
.sec-title{font-size:31px;font-weight:500}
.underline{height:4px;background:var(--yellow);border-radius:2px}
.prod{position:absolute;width:218px;text-align:center}
.prod .tile{height:211px;border-radius:20px;
  background:radial-gradient(ellipse 80px 90px at 50% 50%,rgba(120,120,120,.45),rgba(120,120,120,0) 80%),var(--tile)}
.prod h3{font-size:20px;font-weight:500;margin-top:33px}
.prod .price{font-size:18px;font-weight:500;margin-top:8px}
.btn{display:inline-block;background:var(--yellow);color:var(--ink);border-radius:20px;font-weight:500}
.prod .btn{margin-top:16px;width:128px;height:40px;line-height:40px;font-size:15px}

/* about */
.about-img{border-radius:22px}
.about h2{font-size:33px;font-weight:500}
.about p{font-size:17px;line-height:27px}

/* reviews */
.reviews{left:0;top:2724px;width:1200px;height:513px;
  background:
    radial-gradient(ellipse 300px 260px at 1150px 420px,rgba(120,90,50,.7),rgba(120,90,50,0) 70%),
    radial-gradient(ellipse 360px 200px at 180px 120px,rgba(50,80,55,.8),rgba(50,80,55,0) 70%),
    linear-gradient(135deg,#243426 0%,#1a211c 45%,#22211f 75%,#3a2e20 100%)}
.rcard{position:absolute;top:161px;width:523px;height:242px;background:rgba(85,90,85,.5);border-radius:22px;color:#eee}
.rcard .quote{position:absolute;left:22px;top:18px}
.rcard p{position:absolute;left:72px;top:52px;width:430px;font-size:14.5px;line-height:30px}
.rcard .who{font-weight:700;color:var(--white)}

/* footer */
.footer h4{color:var(--yellow);font-size:18px;font-weight:700}
.footer p,.footer li{font-size:15px;line-height:18px;list-style:none;font-weight:500}
.social{width:34px;height:34px;border-radius:50%;background:var(--black);border:3px solid var(--white);box-shadow:0 0 0 2px var(--black)}
.newsletter{left:770px;top:3444px;width:362px;height:39px;border-radius:20px;background:#2e2e2e;color:#ddd;font-size:13px;padding:11px 18px}
</style>
</head>
<body>

<!-- Hero -->
<section class="abs hero" role="img" aria-label="Foto: Wohnraum mit Fenster und heruntergelassener Senkrechtmarkise"></section>
<div class="abs hero-shade"></div>
<div class="abs hero-bar"></div>
<nav class="nav">
  <a style="left:577px">Home</a>
  <a style="left:671px">Über uns</a>
  <a style="left:782px">Unsere Produkte</a>
  <a style="left:949px">Leistungen</a>
  <a style="left:1077px">Kontakt</a>
</nav>
<div class="abs brand"><span class="brand-mark"></span><span class="brand-name">WANDELRAUM</span></div>
<h1 class="abs hero-title center">SENKRECHTMARKISEN ZIP 6</h1>
<div class="abs hero-sub center"><b>SCHLICHT</b> UND EXKLUSIV</div>
<p class="abs hero-text center">Beschattete Fenster bis zu 6 Meter Breite. Mit Kassetten gleicher Abmessungen<br>für eine einheitliche Optik – eine vielseitige Lösung für hohe Ansprüche.</p>
<div class="abs dots center" style="left:0;width:1200px;top:627px">
  <span style="background:#ccc"></span><span style="background:#fff"></span><span style="background:#fff"></span>
</div>

<!-- Partners -->
<section class="abs partners">
  <h2>Mehr als 200 großartige Unternehmen<br>weltweit vertrauen uns</h2>
  <svg class="arrow" style="left:1055px;top:42px" width="30" height="16" viewBox="0 0 30 16"><path d="M29 8H2M9 1L2 8l7 7" fill="none" stroke="#fff" stroke-width="2"/></svg>
  <svg class="arrow" style="left:1100px;top:42px" width="30" height="16" viewBox="0 0 30 16"><path d="M1 8h27M21 1l7 7-7 7" fill="none" stroke="#fff" stroke-width="2"/></svg>

  <div class="pcard" style="left:66px;top:168px">
    <div class="photo" role="img" aria-label="Foto: Wohnbereich mit Schiebeläden vor der Fensterfront" style="background:radial-gradient(ellipse 140px 60px at 50% 85%,rgba(200,180,140,.9),rgba(200,180,140,0) 80%),linear-gradient(#6f6a5e 0%,#a39b88 45%,#8a7e66 100%)"></div>
    <h3>Insektenschutz-Schiebetür</h3>
    <p>Beschattete Fenster bis zu 6 Meter<br>Breite. Mit Kassetten gleicher.</p>
  </div>
  <div class="pcard" style="left:434px;top:264px">
    <div class="photo" role="img" aria-label="Foto: Raum mit großem Panoramafenster und Gartenblick" style="background:linear-gradient(#cfd3d4 0%,#b8c2c6 35%,#7f8f5c 60%,#5d6e3e 75%,#c9c4bb 100%)"></div>
    <h3>Panoramafenster</h3>
    <p>Beschattete Fenster bis zu 6 Meter<br>Breite. Mit Kassetten gleicher.</p>
  </div>
  <div class="pcard" style="left:800px;top:168px">
    <div class="photo" role="img" aria-label="Foto: Moderne Hausfassade mit Rollläden" style="background:linear-gradient(#dfe6ee 0%,#f2f3f4 30%,#8a8d92 45%,#4a4c50 80%,#6b6d70 100%)"></div>
    <h3 style="margin-top:20px">Rollläden</h3>
    <p>Beschattete Fenster bis zu 6 Meter<br>Breite. Mit Kassetten gleicher.</p>
  </div>
</section>

<!-- Products -->
<section class="abs products">
  <h2 class="abs sec-title center" style="left:0;width:1200px;top:78px">Meistverkaufte Produkte</h2>
  <div class="abs underline" style="left:573px;top:121px;width:54px"></div>

  <div class="prod" style="left:66px;top:193px">
    <div class="tile" role="img" aria-label="Produktbild: Rollladen mit Kasten"></div>
    <h3>Rollladen</h3><div class="price">$800</div><span class="btn">Kaufe Jetzt</span>
  </div>
  <div class="prod" style="left:349px;top:193px">
    <div class="tile" role="img" aria-label="Produktbild: Pergola-Markise"></div>
    <h3>Pergola-Markisen</h3><div class="price">$800</div><span class="btn">Kaufe Jetzt</span>
  </div>
  <div class="prod" style="left:630px;top:193px">
    <div class="tile" role="img" aria-label="Produktbild: Insektenschutztür"></div>
    <h3>Insektenschutztür</h3><div class="price">$800</div><span class="btn">Kaufe Jetzt</span>
  </div>
  <div class="prod" style="left:916px;top:193px">
    <div class="tile" role="img" aria-label="Produktbild: Insektenschutzgitter im Rahmen"></div>
    <h3>Insektenschutztür</h3><div class="price">$800</div><span class="btn">Kaufe Jetzt</span>
  </div>

  <div class="abs dots center" style="left:0;width:1200px;top:604px">
    <span style="background:#111"></span><span style="background:#111"></span><span style="background:#111"></span>
  </div>

  <!-- About -->
  <div class="about">
    <div class="abs about-img" role="img" aria-label="Foto: Heller Wohnraum mit Treppe und großer Glasfront" style="left:66px;top:831px;width:316px;height:411px;background:radial-gradient(ellipse 160px 120px at 40% 20%,rgba(250,250,248,.9),rgba(250,250,248,0) 75%),linear-gradient(#d8d8d5 0%,#a9a9a5 45%,#55524e 80%,#3a3835 100%)"></div>
    <div class="abs about-img" role="img" aria-label="Foto: Wohnzimmer mit raumhohen Fenstern" style="left:314px;top:904px;width:181px;height:236px;background:linear-gradient(#d9dcd8 0%,#8f9a86 40%,#4b5446 70%,#262824 100%)"></div>
    <div class="abs about-img" role="img" aria-label="Foto: Arbeitsbereich vor großem Fenster" style="left:99px;top:1070px;width:184px;height:233px;background:linear-gradient(#c2c6c6 0%,#8d9390 40%,#4a4844 70%,#2b2926 100%)"></div>

    <h2 class="abs" style="left:600px;top:884px">Wer Wir Sind</h2>
    <div class="abs underline" style="left:600px;top:926px;width:58px"></div>
    <p class="abs" style="left:600px;top:953px;width:500px">Beschattete Fenster bis zu 6 Meter Breite. Mit Kassetten gleicher Abmessungen für eine einheitliche Optik – eine vielseitige Lösung für hohe Ansprüche.Beschattete Fenster bis zu 6 Meter Breite. Mit Kassetten gleicher.</p>
    <p class="abs" style="left:600px;top:1088px;width:500px">Abmessungen für eine einheitliche Optik – eine vielseitige Lösung für hohe Ansprüche.</p>
    <span class="abs btn center" style="left:600px;top:1198px;width:154px;height:40px;line-height:40px;font-size:17px">Mehr wissen</span>
  </div>
</section>

<!-- Reviews -->
<section class="abs reviews" role="img" aria-label="Hintergrundfoto: dunkle moderne Küche">
  <h2 class="abs sec-title center" style="left:0;width:1200px;top:74px;color:#fff">Kundenbewertungen</h2>
  <svg class="arrow" style="left:1055px;top:99px" width="30" height="16" viewBox="0 0 30 16"><path d="M29 8H2M9 1L2 8l7 7" fill="none" stroke="#fff" stroke-width="2"/></svg>
  <svg class="arrow" style="left:1100px;top:99px" width="30" height="16" viewBox="0 0 30 16"><path d="M1 8h27M21 1l7 7-7 7" fill="none" stroke="#fff" stroke-width="2"/></svg>

  <div class="rcard" style="left:66px">
    <svg class="quote" width="44" height="36" viewBox="0 0 44 36"><path d="M2 34V20C2 10 7 4 16 2l2 5c-5 2-7 5-7 9h7v18zM25 34V20c0-10 5-16 14-18l2 5c-5 2-7 5-7 9h7v18z" fill="#fcc30b"/></svg>
    <p>Steht für hohe Qualität, attraktives Design und individuelle, maßgeschneiderte Kundenlösungen. Langjährige Expertise und Liebe zum Detail schaffen Wohlfühlprodukte der Extraklasse. Eine industrielle Manufaktur, die intelligente Innovationen in einem vielseitigen Spektrum zum Ausdruck bringt.<br><span class="who">Mira - CEO</span></p>
  </div>
  <div class="rcard" style="left:609px">
    <svg class="quote" width="44" height="36" viewBox="0 0 44 36"><path d="M2 34V20C2 10 7 4 16 2l2 5c-5 2-7 5-7 9h7v18zM25 34V20c0-10 5-16 14-18l2 5c-5 2-7 5-7 9h7v18z" fill="#fcc30b"/></svg>
    <p>Steht für hohe Qualität, attraktives Design und individuelle, maßgeschneiderte Kundenlösungen. Langjährige Expertise und Liebe zum Detail schaffen Wohlfühlprodukte der Extraklasse. Eine industrielle Manufaktur, die intelligente Innovationen in einem vielseitigen Spektrum zum Ausdruck bringt.<br><span class="who">Mira - CEO</span></p>
  </div>
  <div class="abs dots center" style="left:0;width:1200px;top:430px">
    <span style="background:#555"></span><span style="background:#555"></span><span style="background:#555"></span>
  </div>
</section>

<!-- Footer -->
<footer class="footer">
  <h4 class="abs" style="left:66px;top:3355px">WANDELRAUM</h4>
  <p class="abs" style="left:66px;top:3392px;width:200px">Konrad Faunitz<br>Erlenstieg 14 24100,<br>Kielbach</p>
  <p class="abs" style="left:66px;top:3465px">Telefon 0160 55512340</p>
  <p class="abs" style="left:66px;top:3501px">k.faunitz@wandelraum-fenster.de</p>
  <div class="abs social" style="left:67px;top:3551px" aria-label="Soziales Netzwerk"></div>
  <div class="abs social" style="left:108px;top:3551px" aria-label="Soziales Netzwerk"></div>
  <div class="abs social" style="left:149px;top:3551px" aria-label="Soziales Netzwerk"></div>
  <div class="abs social" style="left:189px;top:3551px" aria-label="Soziales Netzwerk"></div>
  <div class="abs social" style="left:230px;top:3551px" aria-label="Soziales Netzwerk"></div>

  <h4 class="abs" style="left:466px;top:3355px">Quicklinks</h4>
  <ul class="abs" style="left:466px;top:3392px">
    <li style="line-height:27px">Home</li><li style="line-height:27px">Über uns</li><li style="line-height:27px">Unsere Produkte</li><li style="line-height:27px">Leistungen</li><li style="line-height:27px">Kontakt</li>
  </ul>

  <h4 class="abs" style="left:770px;top:3355px">Newsletter</h4>
  <p class="abs" style="left:770px;top:3392px;width:300px">Morbi tristique, felis et ullamcorper fermentum, mi neque pulvinar mauris,</p>
  <div class="abs newsletter">deine E-Mail</div>
  <svg class="abs" style="left:1093px;top:3457px" width="20" height="12" viewBox="0 0 20 12"><path d="M1 6h17M13 1l5 5-5 5" fill="none" stroke="#fff" stroke-width="1.5"/></svg>
</footer>

</body>
</html>
```